Hearth Keepers Brochure - marketing an innovative home maintenance subscription program

We would like a brochure for this new service offering.
Hearth Keepers offers a subscription based home maintenance program that is quite unique. Everyone goes to the dentist for regular checkups and cleanings, or takes their car for oil changes, but too few pay that much attention to their largest asset - their home. So we fill that niche. We need a good brochure to promote the quarterly maintenance and our general contracting services.

Target Market(s)

Upper-Middle Class, SF Bay Area, Home Owner. Techies without know-how or time, single women, and elderly families or those with vacation homes.

Industry/Entity Type

Handyman and general contracting (residential construction and maintenance)

Font styles to use
Serif

Colors
0054AA
0677BA
7BADD7
CADEEF
E8F1F8

Requirements
Must have
• Basic contact info for www.HearthKeepers.example, some sort of hook, logo, etc.
Nice to have
• Something awesome!
Should not have
• Want classy, not cheap or flashy. Must have good balance for high-end homeowners in San Francisco Bay Area.

```html
<!DOCTYPE html>
<html lang="en">
<head>
<meta charset="utf-8">
<title>Hearth Keepers Tri-fold Brochure</title>
<link href="https://fonts.googleapis.com/css2?family=Oswald:wght@500;600;700&family=Open+Sans:wght@400;600;700;800&display=swap" rel="stylesheet">
<style>
  :root{
    --navy:#203f95;
    --navy-dark:#172f73;
    --gold:#f6b51e;
    --orange:#f08a1c;
    --ink:#2b2b33;
    --paper:#ffffff;
    --stage:#e6e7e9;
    --sky:#7badd7;
  }
  *{box-sizing:border-box;margin:0;padding:0}
  html,body{width:1200px;height:2400px;overflow:hidden}
  body{background:var(--stage);font-family:"Open Sans",Arial,sans-serif;color:var(--ink);position:relative}
  .spread{position:absolute;left:50px;width:1100px;height:850px;background:var(--paper);box-shadow:0 6px 24px rgba(0,0,0,.18);overflow:hidden}
  .spread--outside{top:275px}
  .spread--inside{top:1275px}
  .panel{position:absolute;top:0;height:850px;overflow:hidden}
  .panel--left{left:0;width:367px}
  .panel--middle{left:367px;width:366px}
  .panel--right{left:733px;width:367px}
  .fold{position:absolute;top:0;width:1px;height:850px;background:rgba(0,0,0,.06);z-index:5}

  .photo{position:absolute;display:block}
  .house-edge{position:absolute;left:0;width:100%;display:block}

  .brand{display:flex;align-items:center;gap:10px}
  .brand__mark{width:34px;height:34px;background:var(--navy);flex:none}
  .brand__name{font-family:"Oswald",Arial,sans-serif;font-weight:700;color:var(--navy);text-transform:uppercase;line-height:1}

  .band{position:absolute;left:0;bottom:0;width:100%;height:56px;background:var(--navy);display:flex;align-items:center;gap:10px;padding-left:26px;color:#fff;font-weight:700;font-size:16px}
  .band__globe{width:22px;height:22px}

  /* outside left */
  .gc{position:absolute;left:30px;right:26px;top:340px}
  .gc__title{font-family:"Oswald",Arial,sans-serif;font-weight:600;font-size:24px;color:var(--navy);letter-spacing:.5px;margin:14px 0 10px}
  .gc__intro{font-size:11.5px;line-height:1.45;margin-bottom:10px}
  .gc__list{list-style:none}
  .gc__list li{display:flex;align-items:center;gap:10px;font-size:11.5px;margin-bottom:7px}
  .tick{width:20px;height:20px;flex:none}
  .gc__note{font-size:11.5px;line-height:1.45;margin-top:10px}

  /* outside middle */
  .panel--blue{background:var(--navy);color:#fff;text-align:center}
  .circle-photo{position:absolute;border-radius:50%;border:5px solid var(--gold)}
  .promo{position:absolute;left:30px;right:30px;top:225px}
  .promo__title{font-family:"Oswald",Arial,sans-serif;font-weight:600;font-size:22px;line-height:1.2;color:var(--gold);text-transform:uppercase}
  .promo__text{font-size:11.5px;line-height:1.5;margin:12px 0 16px}
  .promo__cta{font-weight:800;font-size:12px;text-transform:uppercase;line-height:1.35}
  .phone-pill{display:inline-flex;align-items:center;gap:10px;margin:12px 0 14px;background:var(--gold);color:var(--navy);border-radius:24px;padding:8px 28px;font-weight:800;font-size:20px}
  .phone-pill svg{width:20px;height:20px}
  .dots{display:flex;justify-content:center;gap:6px;margin-bottom:20px}
  .dots span{width:9px;height:9px;border-radius:50%;background:var(--gold)}
  .promo__url{position:absolute;left:0;right:0;bottom:34px;font-weight:700;font-size:16px;color:var(--gold)}

  /* cover */
  .cover-brand{position:absolute;left:28px;top:575px}
  .cover-brand .brand__mark{width:70px;height:70px}
  .cover-brand .brand__name{font-size:46px}
  .cover-tagline{position:absolute;left:28px;right:20px;top:670px;font-family:"Oswald",Arial,sans-serif;font-weight:600;font-size:25px;line-height:1.15;color:var(--ink);text-transform:uppercase}

  /* inside left */
  .program{position:absolute;left:26px;right:24px;top:28px;color:#fff}
  .program__title{font-family:"Oswald",Arial,sans-serif;font-weight:700;font-size:26px;color:var(--gold);text-transform:uppercase;margin-bottom:12px}
  .program__lead{font-weight:800;font-size:13px;line-height:1.35;text-transform:uppercase;margin-bottom:10px}
  .program__intro{font-size:11px;line-height:1.45;margin-bottom:12px}
  .steps{list-style:none}
  .steps li{display:flex;gap:10px;font-size:10.5px;line-height:1.4;margin-bottom:9px}
  .steps .badge{width:22px;height:22px;flex:none;background:var(--gold);border-radius:3px}
  .program__photos{position:absolute;left:26px;right:24px;top:680px;display:flex;gap:10px}
  .program__photos .photo{position:static;width:50%;height:82px}
  .partner{position:absolute;left:0;bottom:0;width:100%;height:58px;background:#fff;display:flex;align-items:center;padding-left:26px}
  .partner__badge{width:120px;height:30px;background:var(--navy);border-radius:2px}

  /* inside middle + right */
  .inner-brand{position:absolute;left:397px;top:392px}
  .inner-brand .brand__mark{width:44px;height:44px}
  .inner-brand .brand__name{font-size:30px}
  .inner-head{position:absolute;left:397px;top:452px;font-family:"Oswald",Arial,sans-serif;font-weight:600;font-size:25px;color:var(--navy);text-transform:uppercase;white-space:nowrap}
  .features{position:absolute;list-style:none;top:505px;width:318px}
  .features--middle{left:397px}
  .features--right{left:760px;width:310px}
  .features li{display:flex;gap:12px;font-size:11px;line-height:1.45;margin-bottom:14px}
  .icon-box{width:30px;height:30px;flex:none;background:var(--navy);border-radius:4px;display:flex;align-items:center;justify-content:center}
  .icon-box svg{width:18px;height:18px}
  .emergency{display:flex;align-items:center;gap:12px;font-weight:700;font-size:12px}
  .emergency__tag{background:var(--navy);color:#fff;font-weight:800;font-size:12px;width:30px;height:30px;display:flex;align-items:center;justify-content:center;border-radius:4px;flex:none}
  .inner-phone{display:flex;align-items:center;justify-content:flex-end;gap:8px;color:var(--navy);font-weight:800;font-size:18px;margin-top:6px}
  .inner-phone svg{width:18px;height:18px}
  .cta-band{position:absolute;left:397px;right:0;bottom:30px;height:44px;background:var(--navy);border-radius:22px 0 0 22px;color:#fff;font-weight:800;font-size:13px;letter-spacing:.3px;display:flex;align-items:center;justify-content:center;text-transform:uppercase}
</style>
</head>
<body>

<section class="spread spread--outside">
  <!-- inner flap: general contracting -->
  <div class="panel panel--left">
    <div class="photo" role="img" aria-label="Photo of friends relaxing together on a home patio" style="left:0;top:0;width:367px;height:300px;background:linear-gradient(135deg,#4a5a3a,#a88a66 55%,#e8d6c2)"></div>
    <svg class="house-edge" style="top:230px;height:80px" viewBox="0 0 367 80" preserveAspectRatio="none" aria-hidden="true">
      <path d="M0 80 V40 H60 L100 5 L130 30 V15 H145 V42 L165 60 H367 V80 Z" fill="#fff"/>
    </svg>
    <div class="gc">
      <div class="brand"><span class="brand__mark"></span><span class="brand__name" style="font-size:20px">Hearth Keepers</span></div>
      <h3 class="gc__title">GENERAL CONTRACTING</h3>
      <p class="gc__intro">Hearth Keepers can also help with larger home improvement projects such as:</p>
      <ul class="gc__list">
        <li><svg class="tick" viewBox="0 0 20 20"><rect width="20" height="20" rx="3" fill="#f08a1c"/><path d="M5 10l3 3 7-7" stroke="#fff" stroke-width="2.2" fill="none"/></svg>Kitchen and bath remodels</li>
        <li><svg class="tick" viewBox="0 0 20 20"><rect width="20" height="20" rx="3" fill="#f08a1c"/><path d="M5 10l3 3 7-7" stroke="#fff" stroke-width="2.2" fill="none"/></svg>Deck and patio installation</li>
        <li><svg class="tick" viewBox="0 0 20 20"><rect width="20" height="20" rx="3" fill="#f08a1c"/><path d="M5 10l3 3 7-7" stroke="#fff" stroke-width="2.2" fill="none"/></svg>Windows, siding, doors and trim</li>
        <li><svg class="tick" viewBox="0 0 20 20"><rect width="20" height="20" rx="3" fill="#f08a1c"/><path d="M5 10l3 3 7-7" stroke="#fff" stroke-width="2.2" fill="none"/></svg>Dry rot repair</li>
        <li><svg class="tick" viewBox="0 0 20 20"><rect width="20" height="20" rx="3" fill="#f08a1c"/><path d="M5 10l3 3 7-7" stroke="#fff" stroke-width="2.2" fill="none"/></svg>Home comfort and HVAC upgrades</li>
        <li><svg class="tick" viewBox="0 0 20 20"><rect width="20" height="20" rx="3" fill="#f08a1c"/><path d="M5 10l3 3 7-7" stroke="#fff" stroke-width="2.2" fill="none"/></svg>Indoor air quality improvements</li>
      </ul>
      <p class="gc__note">We specialize in remodeling, deferred maintenance and proven healthy building practices.</p>
    </div>
    <div class="band">
      <svg class="band__globe" viewBox="0 0 22 22"><circle cx="11" cy="11" r="9" fill="none" stroke="#fff" stroke-width="1.8"/><path d="M2 11h18M11 2c-4 5-4 13 0 18M11 2c4 5 4 13 0 18" fill="none" stroke="#fff" stroke-width="1.4"/></svg>
      www.hearthkeepers.example
    </div>
  </div>

  <!-- back panel -->
  <div class="panel panel--middle panel--blue">
    <div class="circle-photo" role="img" aria-label="Photo of a technician with a tool bag servicing a home" style="left:108px;top:40px;width:150px;height:150px;background:radial-gradient(circle at 40% 40%,#e6e1d8,#8a8f99 70%,#3b3f4a)"></div>
    <div class="promo">
      <h2 class="promo__title">Your one-stop-shop for home maintenance and repairs</h2>
      <p class="promo__text">Hearth Keepers is a professional handyman and general contracting firm, a division of Sound Frame Science. Serving the Bay Area since 2001. We are a B Corp.</p>
      <p class="promo__cta">Call today or click here to schedule<br>a free initial consultation</p>
      <div class="phone-pill">
        <svg viewBox="0 0 20 20"><path d="M5 2l3 3-2 2c1 2.5 3 4.5 5 5.5l2-2 3 3-2 3C8 16 4 12 2 5z" fill="#203f95"/></svg>
        (415) 555-0142
      </div>
      <div class="dots"><span></span><span></span><span></span></div>
      <h2 class="promo__title" style="font-size:18px">We have a system that works to keep your home running smoothly!</h2>
      <p class="promo__text">No more worrying about if you changed the air filters in time, or cleaned the gutters before the winter rains. We help you care for your home.</p>
    </div>
    <div class="promo__url">www.hearthkeepers.example</div>
  </div>

  <!-- front cover -->
  <div class="panel panel--right">
    <div class="photo" role="img" aria-label="Photo of a worker on a ladder cleaning the gutters of a white house" style="left:0;top:0;width:367px;height:500px;background:linear-gradient(160deg,#f3c58a,#d9d6cf 40%,#6d7383 75%,#2f3a5c)"></div>
    <svg class="house-edge" style="top:400px;height:120px" viewBox="0 0 367 120" preserveAspectRatio="none" aria-hidden="true">
      <path d="M0 120 V70 H50 L95 30 V10 H115 V22 L140 0 L210 60 H367 V120 Z" fill="#fff"/>
    </svg>
    <div class="brand cover-brand"><span class="brand__mark"></span><span class="brand__name">Hearth Keepers</span></div>
    <p class="cover-tagline">We maintain your home, so you don't have to.</p>
    <div class="band">
      <svg class="band__globe" viewBox="0 0 22 22"><circle cx="11" cy="11" r="9" fill="none" stroke="#fff" stroke-width="1.8"/><path d="M2 11h18M11 2c-4 5-4 13 0 18M11 2c4 5 4 13 0 18" fill="none" stroke="#fff" stroke-width="1.4"/></svg>
      www.hearthkeepers.example
    </div>
  </div>
  <span class="fold" style="left:367px"></span><span class="fold" style="left:733px"></span>
</section>

<section class="spread spread--inside">
  <div class="panel panel--left" style="background:var(--navy)">
    <div class="program">
      <h2 class="program__title">Hearth Keepers</h2>
      <p class="program__lead">Hearth Keepers offers an amazing proactive maintenance program.</p>
      <p class="program__intro">We keep one of your largest assets in great condition and let you enjoy your weekends. This system has been perfected for over 20 years. Here's how it works:</p>
      <ul class="steps">
        <li><span class="badge"></span>During an initial intake inspection we inventory all major systems and appliances, and generate a punch list of any deferred maintenance.</li>
        <li><span class="badge"></span>Using this information we can respond more quickly when things break, and we create a roadmap to address any problems.</li>
        <li><span class="badge"></span>Then, using seasonal checklists, a team member comes quarterly to inspect and repair over 250 items of wear.</li>
        <li><span class="badge"></span>Our GC Division manages any larger repairs or special projects.</li>
        <li><span class="badge"></span>Financial advisors recommend budgeting 1-4% of the value of a home for annual maintenance.</li>
        <li><span class="badge"></span>Hearth keeping is the most cost-efficient way to maintain your home.</li>
      </ul>
    </div>
    <div class="program__photos">
      <div class="photo" role="img" aria-label="Photo of a crew repairing a roof" style="background:linear-gradient(135deg,#c9b78f,#6f6a5a)"></div>
      <div class="photo" role="img" aria-label="Photo of a technician working on a home exterior" style="background:linear-gradient(135deg,#a9b4c4,#4d5566)"></div>
    </div>
    <div class="partner"><span class="partner__badge"></span></div>
  </div>

  <div class="photo" role="img" aria-label="Photo of a modern house with a lit patio at dusk" style="left:367px;top:0;width:733px;height:380px;background:linear-gradient(120deg,#3d4b34,#8a7a5e 40%,#d9cbb0 65%,#f1ece2)"></div>
  <svg class="house-edge" style="left:367px;top:300px;width:733px;height:110px" viewBox="0 0 733 110" preserveAspectRatio="none" aria-hidden="true">
    <path d="M0 110 V70 H90 L150 20 V5 H172 V20 L200 0 L290 60 H733 V110 Z" fill="#fff"/>
  </svg>
  <div class="circle-photo" role="img" aria-label="Photo of a technician inspecting a home appliance" style="left:960px;top:300px;width:110px;height:110px;border-color:var(--navy);background:radial-gradient(circle at 40% 40%,#e3e6ea,#7d8797 70%,#38404f)"></div>

  <div class="brand inner-brand"><span class="brand__mark"></span><span class="brand__name">Hearth Keepers</span></div>
  <h2 class="inner-head">We maintain your home, so you don't have to.</h2>

  <ul class="features features--middle">
    <li><span class="icon-box"><svg viewBox="0 0 18 18"><path d="M3 9l4 4 8-8" stroke="#fff" stroke-width="2.2" fill="none"/></svg></span>You take your car in for oil changes. You go to the dentist for check-ups.</li>
    <li><span class="icon-box"><svg viewBox="0 0 18 18"><path d="M3 9l4 4 8-8" stroke="#fff" stroke-width="2.2" fill="none"/></svg></span>But when was the last time you had your home inspected, or managed, to check over 250 items off your to-do list?</li>
    <li><span class="icon-box"><svg viewBox="0 0 18 18"><path d="M3 9l4 4 8-8" stroke="#fff" stroke-width="2.2" fill="none"/></svg></span>Hearth keeping is a philosophy and lifestyle change.</li>
    <li><span class="icon-box"><svg viewBox="0 0 18 18"><path d="M3 9l4 4 8-8" stroke="#fff" stroke-width="2.2" fill="none"/></svg></span>We keep your largest asset in great condition, and let you take back your weekends.</li>
  </ul>

  <ul class="features features--right">
    <li><span class="icon-box"><svg viewBox="0 0 18 18"><path d="M3 9l4 4 8-8" stroke="#fff" stroke-width="2.2" fill="none"/></svg></span>Our unique subscription service combines quarterly inspections and handyman repairs.</li>
    <li><span class="icon-box"><svg viewBox="0 0 18 18"><path d="M3 9l4 4 8-8" stroke="#fff" stroke-width="2.2" fill="none"/></svg></span>Don't climb that rickety ladder to clean your gutters or start projects you can't finish.</li>
    <li><span class="icon-box"><svg viewBox="0 0 18 18"><path d="M3 9l4 4 8-8" stroke="#fff" stroke-width="2.2" fill="none"/></svg></span>Our team is ready to care for your home.</li>
    <li class="emergency"><span class="emergency__tag">24/7</span>24/7 Emergency Response</li>
    <li class="inner-phone"><svg viewBox="0 0 20 20"><path d="M5 2l3 3-2 2c1 2.5 3 4.5 5 5.5l2-2 3 3-2 3C8 16 4 12 2 5z" fill="#203f95"/></svg>(415) 555-0142</li>
  </ul>

  <div class="cta-band">Call today or click here to schedule a free initial consultation</div>
  <span class="fold" style="left:367px"></span><span class="fold" style="left:733px"></span>
</section>

</body>
</html>
```